Fresh Website for PLIM and Qulo alliance

Page designs for 11 pages using existing Jigsaw template for the homepage and existing company logo.

Mock-up of front page attached, feel free to turn it into something elegant, professional and clean.

Target Market(s)

1. Small to medium business owners who use DRUK or other accounting software who want to use Qulo.
2 Businesses who want to hire a decent Bookkeeper instead of trying to do it on the kitchen table at night.

Industry/Entity Type

It Company

Font styles to use
Sans Serif

Colors
86cae6
32a6d6
34a7d8
cee9f5

Requirements
Must have
• Use the Qulo blue colour for the website theme - PMS: Blue #00A0C6
Use the Jigsaw template design and theme - pieces of the puzzle all fitting together with Qulo and PLIM
Same font used in the plim blue png uploaded and plimtraining logo
Nice to have
• A style that mirrors and links easily with the Qulo website:
check out www.qulo.com.au
Should not have
• Cheesy pictures of money and $$,
Cluttered feel
Chunky anime like images for buttons icons
Not to scream Jigsaw and make everything look like a kids website - just subtle nods to the theme

```html
<!DOCTYPE html>
<html lang="en">
<head>
<meta charset="utf-8">
<title>Free Initial Consultation – PLIM</title>
<link rel="stylesheet" href="https://fonts.googleapis.com/css2?family=Oswald:wght@400&family=Arimo:wght@400&display=swap">
<style>
  :root {
    --panel-bg: #f8f8f8;
    --panel-border: #e6e6e6;
    --accent-blue: #1a9fc9;
    --body-text: #333333;
    --photo-sky: #c9d8e2;
    --photo-mid: #9fb2bf;
    --photo-light: #eef1f3;
    --photo-folder: #32a6d6;
  }
  html, body {
    margin: 0;
    padding: 0;
    width: 1200px;
    height: 273px;
    overflow: hidden;
    background: #ffffff;
  }
  .consultation-panel {
    position: relative;
    box-sizing: border-box;
    width: 1200px;
    height: 273px;
    background: var(--panel-bg);
    border: 1px solid var(--panel-border);
  }
  .consultation-title {
    position: absolute;
    left: 89px;
    top: 52px;
    margin: 0;
    font-family: "Oswald", "Arial Narrow", sans-serif;
    font-weight: 400;
    font-size: 31px;
    line-height: 1.2;
    color: var(--accent-blue);
    letter-spacing: -0.2px;
  }
  .consultation-copy {
    position: absolute;
    left: 47px;
    top: 113px;
    width: 660px;
    margin: 0;
    font-family: "Arimo", Arial, sans-serif;
    font-size: 11.5px;
    line-height: 21.5px;
    color: var(--body-text);
  }
  .consultation-copy p { margin: 0; }
  .consultation-photo {
    position: absolute;
    left: 743px;
    top: 38px;
    width: 407px;
    height: 210px;
    background:
      linear-gradient(90deg, transparent 0 70%, rgba(255,255,255,0.55) 70% 100%),
      linear-gradient(180deg, var(--photo-sky) 0%, var(--photo-mid) 45%, var(--photo-light) 75%, #ffffff 100%);
  }
</style>
</head>
<body>
  <section class="consultation-panel">
    <h2 class="consultation-title">Free Initial Consultation</h2>
    <div class="consultation-copy">
      <p>Would you like to transform your business with the complete Qulo solution?</p>
      <p>Whether you’re an established company wanting to take your business further or just starting out, PLIM is here to help.</p>
      <p>PLIM offers a free 30-minute strategy session to understand your business issues, identify solutions and create strategies for success.</p>
      <p>To begin, call us on (02) 5550 1847 or</p>
      <p>Email: books@plim.com.au</p>
    </div>
    <div class="consultation-photo" role="img" aria-label="Photo of a smiling consultant holding a blue folder, meeting a client in a bright office with a city view"></div>
  </section>
</body>
</html>
```